Auto Mechanic business card

Need a general business card for GearFixer.
Name on card should be 'Roadside Wrench'
Tel # (869) 412 3097
Address is - Palm Lane, Basseterre, St. Kitts
Whatsapp and facebook symbols should be added
On back of card should include services offered
General Repairs
Brakes
Tune Ups
Suspensions
Oil Leaks
Dent repairs
Suspensions
Car Sales
Tyre Repairs
General service
Check Engine Light
Minor Electricals

Target Market(s)

General Population, University students

Industry/Entity Type

Auto Mechanic

Contact Information for Business Card

Roadside Wrench

Requirements
Must have
• 2 Sides

```html
<!DOCTYPE html>
<html lang="en">
<head>
<meta charset="utf-8">
<title>Roadside Wrench – Business Card</title>
<link rel="stylesheet" href="https://fonts.googleapis.com/css2?family=Orbitron:wght@800&family=Quicksand:wght@500;600&display=swap">
<style>
  :root {
    --page: #5c5f61;
    --card-black: #111112;
    --card-black-light: #1e1f21;
    --brand-red: #c41013;
    --silver-light: #f4f4f4;
    --silver-mid: #b9bbbe;
    --silver-dark: #7d8084;
    --text-white: #ffffff;
  }
  * { box-sizing: border-box; margin: 0; padding: 0; }
  html, body { width: 1200px; height: 780px; overflow: hidden; }
  body {
    background: var(--page);
    position: relative;
    font-family: "Quicksand", sans-serif;
    color: var(--text-white);
  }
  .card {
    position: absolute;
    left: 310px;
    width: 580px;
    height: 331px;
    border-radius: 22px;
    overflow: hidden;
    background: radial-gradient(ellipse at 55% 35%, var(--card-black-light), var(--card-black) 70%);
    box-shadow: 0 10px 24px rgba(0,0,0,0.45);
  }
  .card--front { top: 40px; }
  .card--back { top: 409px; }
  .card__texture {
    position: absolute; inset: 0;
    background: linear-gradient(160deg, rgba(255,255,255,0.04), rgba(0,0,0,0.1));
  }
  .card__band { position: absolute; inset: 0; width: 580px; height: 331px; }

  .brand-title {
    position: absolute;
    left: 0; right: 0; top: 62px;
    text-align: center;
    font-family: "Orbitron", sans-serif;
    font-weight: 800;
    font-size: 46px;
    line-height: 1.12;
    letter-spacing: 1px;
    text-transform: uppercase;
    background: linear-gradient(180deg, var(--silver-light) 0%, var(--silver-mid) 48%, var(--silver-dark) 52%, var(--silver-light) 100%);
    -webkit-background-clip: text;
    background-clip: text;
    color: transparent;
  }

  .contact {
    position: absolute;
    left: 20px; bottom: 14px;
    font-size: 13.5px;
    font-weight: 500;
    font-style: normal;
    letter-spacing: 0.4px;
  }
  .contact__row { display: flex; align-items: center; gap: 10px; height: 22px; }
  .contact__icon { width: 18px; height: 18px; flex: none; }

  .social {
    position: absolute;
    right: 22px; top: 226px;
    display: flex; align-items: center; gap: 7px;
    font-size: 13px; font-weight: 600;
  }
  .social__dot {
    width: 16px; height: 16px; border-radius: 50%;
    border: 2px solid var(--text-white);
  }

  .services-heading {
    position: absolute;
    left: 150px; top: 18px;
    width: 300px;
    font-family: "Orbitron", sans-serif;
    font-weight: 800;
    font-size: 22px;
    text-align: center;
    padding-bottom: 7px;
    border-bottom: 1px solid var(--silver-dark);
  }
  .services-heading__accent { color: var(--brand-red); }
  .services-list {
    position: absolute;
    top: 66px;
    list-style: none;
    font-size: 15.5px;
    font-weight: 500;
    line-height: 21px;
  }
  .services-list--left { left: 60px; }
  .services-list--right { left: 315px; }
  .services-list li { display: flex; align-items: center; gap: 10px; }
  .services-list li::before {
    content: "";
    width: 0; height: 0;
    border-left: 6px solid transparent;
    border-right: 6px solid transparent;
    border-top: 9px solid var(--brand-red);
  }
</style>
</head>
<body>

<svg width="0" height="0" style="position:absolute">
  <defs>
    <linearGradient id="silver-stripe" x1="0" y1="0" x2="1" y2="0">
      <stop offset="0" stop-color="#8a8d91"/>
      <stop offset="0.45" stop-color="#f6f6f6"/>
      <stop offset="0.7" stop-color="#a9acb0"/>
      <stop offset="1" stop-color="#eeeeee"/>
    </linearGradient>
  </defs>
</svg>

<section class="card card--front" aria-label="Front of business card">
  <div class="card__texture" role="img" aria-label="Dark perforated metal texture"></div>
  <svg class="card__band" viewBox="0 0 580 331">
    <polygon points="0,266 580,206 580,216 0,276" fill="url(#silver-stripe)"/>
    <polygon points="0,276 580,216 580,331 0,331" fill="var(--brand-red)"/>
  </svg>
  <h1 class="brand-title">Roadside<br>Wrench</h1>
  <div class="social"><span class="social__dot"></span>GearFixer</div>
  <address class="contact">
    <div class="contact__row">
      <svg class="contact__icon" viewBox="0 0 18 18"><circle cx="9" cy="9" r="9" fill="#fff"/><path d="M6 5.2l1.6-.4 1 2.2-1 .8a5 5 0 0 0 2.6 2.6l.8-1 2.2 1-.4 1.6c-3.8.2-7-3-6.8-6.8z" fill="var(--brand-red)"/></svg>
      <span>(869) 412 3097</span>
    </div>
    <div class="contact__row">
      <svg class="contact__icon" viewBox="0 0 18 18"><circle cx="9" cy="9" r="9" fill="#fff"/><path d="M9 3.8a3.4 3.4 0 0 0-3.4 3.4c0 2.6 3.4 6.6 3.4 6.6s3.4-4 3.4-6.6A3.4 3.4 0 0 0 9 3.8z" fill="var(--brand-red)"/><circle cx="9" cy="7.2" r="1.3" fill="#fff"/></svg>
      <span>Palm Lane, Basseterre, St. Kitts</span>
    </div>
  </address>
</section>

<section class="card card--back" aria-label="Back of business card">
  <div class="card__texture" role="img" aria-label="Dark perforated metal texture"></div>
  <svg class="card__band" viewBox="0 0 580 331">
    <polygon points="0,266 580,206 580,216 0,276" fill="url(#silver-stripe)"/>
    <polygon points="0,276 580,216 580,331 0,331" fill="var(--brand-red)"/>
  </svg>
  <h2 class="services-heading"><span class="services-heading__accent">OUR</span> SERVICES</h2>
  <ul class="services-list services-list--left">
    <li>General Repairs</li>
    <li>Brakes</li>
    <li>Tune Ups</li>
    <li>Suspensions</li>
    <li>Oil Leaks</li>
    <li>Dent repairs</li>
  </ul>
  <ul class="services-list services-list--right">
    <li>Suspensions</li>
    <li>Car Sales</li>
    <li>Tyre Repairs</li>
    <li>General service</li>
    <li>Check Engine Light</li>
    <li>Minor Electricals</li>
  </ul>
  <div class="social"><span class="social__dot"></span>GearFixer</div>
  <address class="contact">
    <div class="contact__row">
      <svg class="contact__icon" viewBox="0 0 18 18"><circle cx="9" cy="9" r="9" fill="#fff"/><path d="M6 5.2l1.6-.4 1 2.2-1 .8a5 5 0 0 0 2.6 2.6l.8-1 2.2 1-.4 1.6c-3.8.2-7-3-6.8-6.8z" fill="var(--brand-red)"/></svg>
      <span>(869) 412 3097</span>
    </div>
    <div class="contact__row">
      <svg class="contact__icon" viewBox="0 0 18 18"><circle cx="9" cy="9" r="9" fill="#fff"/><path d="M9 3.8a3.4 3.4 0 0 0-3.4 3.4c0 2.6 3.4 6.6 3.4 6.6s3.4-4 3.4-6.6A3.4 3.4 0 0 0 9 3.8z" fill="var(--brand-red)"/><circle cx="9" cy="7.2" r="1.3" fill="#fff"/></svg>
      <span>Palm Lane, Basseterre, St. Kitts</span>
    </div>
  </address>
</section>

</body>
</html>
```